Bright Meadow Cabins Needs A Flyer

We need a flyer for our newest product "The Sunlit Garden Workpod Deluxe"

Here is some copy for the flyer:

1. More and more people everyday are working from home and finding it difficult to disconnect from home activities in order to focus on their work. They are also finding it very expensive to add on to their existing house for a quiet place. Our archatectually stunning, Sunlit Garden Workpod Deluxe is the answer. The office studio measures 16' wide and 10' deep. 160 Square feet of space.

Perfect for dozens of purposes. Home office, design studio, artist studio, home school office, reading room, craft studio, drafting room.

Features include:

- Steel Framing. 40-60% lighter then wood, higher strength to weight ratio, resistant to mold and fire and steel is the most recycled material on earth!
- Spray foam insulation. Cool in the summer and warm in the winter.
- HVAC Mini Split with wireless remote control and thermostat.
- 100% Off grid with enough solar and battery storage to run your entire office. No need to pay for an expensive electric installation.
- Flush fitting floor outlets to reduce wires.
- TV mount (Optional with pre-wired electric, HDMI, digital audio & Cat 6)
- Windows are tempered glass custom made by Vorn Glazing.
- Solar qualifies for a 26% tax credit. This is not a write-off rather it is a direct reduction on your tax obligation.
- Thousands of dollars less than adding onto your home.
- Custom color, siding, features available.

This beautiful back yard office is delivered 100% assembled and ready to enjoy on the day of delivery.

We ship nationwide from our factory in South Carolina. Give us a call anytime to speak to a designer and start your dream office today!

555-318-4720
info@BrightMeadowCabins.example

```html
<!DOCTYPE html>
<html lang="en">
<head>
<meta charset="utf-8">
<title>Bright Meadow Cabins – The Sunlit Garden Workpod Deluxe</title>
<link href="https://fonts.googleapis.com/css2?family=Lilita+One&family=Hind:wght@400;500;600;700&display=swap" rel="stylesheet">
<style>
:root{
  --green:#2e7d32;
  --green-dark:#23692a;
  --green-title:#2f8a2f;
  --grass:#4f9a3a;
  --orange:#f2ad1c;
  --ink:#1e1e1e;
  --white:#ffffff;
  --sky-top:#9cc6e8;
  --sky-light:#e7f3fb;
  --tick:#3c9a3c;
}
*{margin:0;padding:0;box-sizing:border-box}
html,body{width:860px;height:1200px;overflow:hidden;background:#fff}
body{font-family:"Hind",sans-serif;color:var(--ink)}
.flyer{position:relative;width:860px;height:1200px;overflow:hidden;
  background:linear-gradient(180deg,#ffffff 540px,var(--sky-light) 700px,#cfe6f6 900px,#bcdcf2 1020px)}
.hero-art{position:absolute;left:0;top:0;width:860px;height:600px}
.headline{position:absolute;left:41px;top:36px;font-family:"Lilita One",sans-serif;
  font-size:37px;line-height:40px;color:var(--green-title);text-transform:uppercase;letter-spacing:.3px}
.brand{position:absolute;left:560px;top:92px;display:flex;align-items:center;gap:10px}
.brand-dot{width:22px;height:22px;border-radius:50%;background:var(--green)}
.brand-name{font-weight:700;font-size:24px;color:var(--orange);line-height:1}
.intro{position:absolute;left:41px;top:558px;width:373px;font-size:13.6px;line-height:17.4px;text-align:justify}
.col-title{font-weight:700;font-size:16px;text-transform:uppercase;letter-spacing:.2px;margin-bottom:4px}
.purposes{position:absolute;left:447px;top:560px;width:380px}
.purposes ul{display:grid;grid-template-columns:152px 200px;row-gap:2px}
.features-title{position:absolute;left:41px;top:710px}
.features{position:absolute;top:737px;width:375px}
.features.left{left:41px}
.features.right{left:447px}
.ticks{list-style:none}
.ticks li{position:relative;padding-left:17px;font-size:13px;line-height:16.4px;margin-bottom:6px}
.features li{text-align:justify}
.purposes .ticks li{font-size:14px;line-height:19px;margin:0}
.ticks li::before{content:"";position:absolute;left:0;top:3px;width:10px;height:10px;border-radius:50%;background:var(--tick)}
.ticks li::after{content:"";position:absolute;left:3px;top:5px;width:4px;height:2.5px;border-left:1.6px solid #fff;border-bottom:1.6px solid #fff;transform:rotate(-45deg)}
.purposes .ticks li::before{top:4px}
.purposes .ticks li::after{top:6px}
.ground{position:absolute;left:0;top:1012px;width:860px;height:141px;
  background:linear-gradient(180deg,var(--grass) 0,#3f8a32 20px,var(--green) 40px,var(--green-dark) 141px)}
.model{position:absolute;top:928px;height:104px;border-radius:2px;
  background:linear-gradient(180deg,#2b2b2b 0,#2b2b2b 10px,#cfd3d3 10px,#9ea3a2 70%,#3a3a3a 100%)}
.model-1{left:43px;width:210px}
.model-2{left:325px;width:204px}
.model-3{left:601px;width:210px}
.ship-note{position:absolute;left:41px;top:1082px;width:420px;color:var(--white);font-weight:600;font-size:14.6px;line-height:19px}
.delivery-box{position:absolute;left:491px;top:1064px;width:326px;height:78px;border:1.6px dashed rgba(255,255,255,.85);
  border-radius:8px;padding:10px 16px;color:var(--white);font-weight:500;font-size:13.4px;line-height:17.6px;text-align:justify}
.contact-bar{position:absolute;left:0;top:1153px;width:860px;height:47px;background:var(--orange);
  display:flex;align-items:center;justify-content:space-between;padding:0 40px 0 41px}
.contact{display:flex;align-items:center;gap:8px;font-weight:500;font-size:16.5px;color:var(--ink)}
.contact svg{width:18px;height:18px;flex:none}
</style>
</head>
<body>
<main class="flyer">
  <svg class="hero-art" viewBox="0 0 860 600" aria-hidden="false">
    <defs>
      <linearGradient id="photoTone" x1="0" y1="0" x2="0" y2="1">
        <stop offset="0" stop-color="#8ebce4"/>
        <stop offset=".28" stop-color="#cfe3ee"/>
        <stop offset=".45" stop-color="#5d7a55"/>
        <stop offset=".7" stop-color="#3f6a34"/>
        <stop offset="1" stop-color="#7c8f70"/>
      </linearGradient>
    </defs>
    <path role="img" aria-label="Photo of a dark-sided garden office studio with glass doors in a landscaped back yard"
          d="M0,0 H860 V470 Q470,486 0,556 Z" fill="url(#photoTone)"/>
    <path d="M0,562 Q470,490 860,476" fill="none" stroke="var(--orange)" stroke-width="9"/>
    <path d="M466,0 Q500,200 860,210 V0 Z" fill="var(--white)"/>
    <path d="M466,0 Q500,200 860,210" fill="none" stroke="var(--orange)" stroke-width="6"/>
  </svg>

  <h1 class="headline">The Sunlit Garden<br>Workpod Deluxe</h1>

  <div class="brand">
    <span class="brand-dot"></span>
    <span class="brand-name">Bright Meadow Cabins</span>
  </div>

  <p class="intro">More and more people everyday are working from home and finding it difficult to disconnect from home activities in order to focus on their work. They are also finding it very expensive to add on to their existing house for a quiet place. Our archatectually stunning, Sunlit Garden Workpod Deluxe is the answer. The office studio measures 16′ wide and 10′ deep. 160 Square feet of space.</p>

  <section class="purposes">
    <h2 class="col-title">Perfect for dozens of purposes.</h2>
    <ul class="ticks">
      <li>Home Office</li><li>Reading Room</li>
      <li>Design Studio</li><li>Drafting Room</li>
      <li>Artist Studio</li><li>Home School Office</li>
      <li>Craft Studio</li>
    </ul>
  </section>

  <h2 class="col-title features-title">Features include:</h2>
  <ul class="ticks features left">
    <li>Steel Framing. 40-60% lighter then wood, higher strength to weight ratio, resistant to mold and fire and steel is the most recycled material on earth!</li>
    <li>Spray foam insulation. Cool in the summer and warm in the winter.</li>
    <li>HVAC Mini Split with wireless remote control &amp; thermostat.</li>
    <li>100% Off grid with enough solar and battery storage to run your entire office. No need to pay for an expensive electric installation.</li>
    <li>Flush fitting floor outlets to reduce wires.</li>
  </ul>
  <ul class="ticks features right">
    <li>TV mount (Optional with pre-wired electric, HDMI, digital audio &amp; Cat 6)</li>
    <li>Windows are tempered glass custom made by Vorn Glazing.</li>
    <li>Solar qualifies for a 26% tax credit. This is not a write-off rather it is a direct reduction on your tax obligation.</li>
    <li>Thousands of dollars less than adding onto your home.</li>
    <li>Custom color, siding, features available.</li>
  </ul>

  <div class="ground"></div>
  <div class="model model-1" role="img" aria-label="Rendering of the workpod seen from the left corner"></div>
  <div class="model model-2" role="img" aria-label="Rendering of the workpod seen from the front"></div>
  <div class="model model-3" role="img" aria-label="Rendering of the workpod seen from the right corner"></div>

  <p class="ship-note">We ship nationwide from our factory in South Carolina.<br>Give us a call anytime to speak to a designer<br>and start your dream office today!</p>
  <p class="delivery-box">This beautiful back yard office is delivered 100% assembled and ready to enjoy on the day of delivery.</p>

  <footer class="contact-bar">
    <span class="contact">
      <svg viewBox="0 0 20 20"><circle cx="10" cy="10" r="10" fill="#1e1e1e"/><path d="M7 5.5l1.6 2.3-1 1.1c.6 1.3 1.5 2.2 2.6 2.7l1.1-1 2.3 1.5-.7 1.7c-3.6-.2-6.6-3.2-6.9-6.8z" fill="#f2ad1c"/></svg>
      555-318-4720
    </span>
    <span class="contact">
      <svg viewBox="0 0 20 20"><circle cx="10" cy="10" r="10" fill="#1e1e1e"/><rect x="5" y="6.5" width="10" height="7" rx="1" fill="#f2ad1c"/><path d="M5.3 7l4.7 3.6L14.7 7" fill="none" stroke="#1e1e1e" stroke-width="1.1"/></svg>
      info@BrightMeadowCabins.example
    </span>
    <span class="contact">
      <svg viewBox="0 0 20 20"><circle cx="10" cy="10" r="10" fill="#1e1e1e"/><g fill="none" stroke="#f2ad1c" stroke-width="1.1"><circle cx="10" cy="10" r="5"/><ellipse cx="10" cy="10" rx="2.2" ry="5"/><path d="M5 10h10"/></g></svg>
      www.BrightMeadowCabins.example
    </span>
  </footer>
</main>
</body>
</html>
```